Voltline Assemblies, Inc. Business Card

Voltline has three operating entities and I'm looking for a standard business card template that can be used for Voltline and the three operating entities that the logo just get swapped out, but has a very similar look and feel. Ultimately if someone had a business card from each, they assume the organizations are related because they all have the same look and feel.
Below are our websites and I will attached the logos for each entity:
https://www.voltlineassemblies.example/
https://www.brantoceramic.example/
https://www.omra-kfsd.example/
https://www.summitbreaker.example/

Target Market(s)

US Voltline

Industry/Entity Type

US Voltline

Contact Information for Business Card

Normal stuff

```html
<!DOCTYPE html>
<html lang="en">
<head>
<meta charset="utf-8">
<title>Voltline Assemblies, Inc. Business Card</title>
<link href="https://fonts.googleapis.com/css2?family=Archivo:wght@700;800&family=Montserrat:wght@400;500&display=swap" rel="stylesheet">
<style>
  :root {
    --navy: #243165;
    --navy-soft: #2e3868;
    --red: #c11f33;
    --white: #ffffff;
    --ink: #3a3a3a;
    --page: #ffffff;
    --fold: #d9dbe2;
  }
  html, body {
    margin: 0;
    padding: 0;
    width: 1200px;
    height: 1200px;
    overflow: hidden;
    background: var(--page);
  }
  .sheet {
    position: relative;
    width: 1200px;
    height: 1200px;
  }
  .card {
    position: absolute;
    left: 177.5px;
    width: 852.5px;
    height: 487px;
    display: block;
    box-shadow: 0 6px 22px rgba(0, 0, 0, 0.18);
  }
  .card--front { top: 95px; }
  .card--back { top: 626px; }
  .holder-name {
    font-family: "Archivo", Arial, sans-serif;
    font-weight: 800;
    font-size: 52px;
    fill: var(--navy);
  }
  .holder-title {
    font-family: "Montserrat", Arial, sans-serif;
    font-weight: 500;
    font-size: 38px;
    letter-spacing: 2px;
    fill: var(--red);
  }
  .contact-line {
    font-family: "Montserrat", Arial, sans-serif;
    font-weight: 500;
    font-size: 32px;
    fill: var(--ink);
  }
  .web-address {
    font-family: "Montserrat", Arial, sans-serif;
    font-weight: 500;
    font-size: 32px;
    letter-spacing: 1.5px;
    fill: var(--white);
  }
  .brand-name {
    font-family: "Archivo", Arial, sans-serif;
    font-weight: 800;
    font-size: 64px;
    text-anchor: middle;
  }
  .brand-name--navy { fill: var(--navy); }
  .brand-name--white { fill: var(--white); }
</style>
</head>
<body>
<main class="sheet">

  <svg class="card card--front" viewBox="0 0 1364 779" xmlns="http://www.w3.org/2000/svg" aria-label="Business card front">
    <rect width="1364" height="779" fill="var(--white)"/>
    <polygon class="band-top" points="0,0 1364,0 1364,152 804,152 719,62 0,62" fill="var(--navy)"/>
    <polygon class="band-bottom" points="0,570 537,570 669,709 1364,709 1364,779 0,779" fill="var(--navy)"/>
    <line class="fold-line" x1="804" y1="156" x2="537" y2="570" stroke="var(--fold)" stroke-width="4"/>
    <line class="fold-line" x1="806" y1="155" x2="1364" y2="155" stroke="var(--fold)" stroke-width="4"/>

    <text class="holder-name" x="114" y="193">DANIEL HARPER</text>
    <text class="holder-title" x="116" y="231">Title</text>

    <g class="icon icon-phone" fill="var(--red)" transform="translate(116,282)">
      <path d="M4 2 C8 0 11 2 12 6 L13 9 C13 11 11 12 10 13 C11 17 13 20 16 22 C17 21 19 19 21 20 L24 22 C26 24 25 27 22 29 C14 30 4 18 4 2 Z"/>
    </g>
    <text class="contact-line" x="163" y="308">+000-1234-5678</text>

    <g class="icon icon-mail" transform="translate(114,344)">
      <rect width="26" height="18" rx="2" fill="var(--red)"/>
      <polyline points="2,3 13,11 24,3" fill="none" stroke="var(--white)" stroke-width="2.5"/>
    </g>
    <text class="contact-line" x="163" y="363">youremail@email.com</text>

    <g class="icon icon-pin" transform="translate(117,399)">
      <path d="M9 0 C15 0 19 4 19 10 C19 16 9 27 9 27 C9 27 0 16 0 10 C0 4 4 0 9 0 Z" fill="var(--red)"/>
      <circle cx="9.5" cy="9.5" r="3.5" fill="var(--white)"/>
    </g>
    <text class="contact-line" x="163" y="425">123 Main Street</text>
    <text class="contact-line" x="163" y="458">11th Floor, Some City</text>

    <text class="web-address" x="112" y="680">voltlineassemblies.example</text>

    <circle class="brand-dot" cx="1004" cy="372" r="72" fill="var(--navy)"/>
    <text class="brand-name brand-name--navy" x="1004" y="530">VOLTLINE</text>
    <text class="brand-name brand-name--navy" x="1004" y="592" style="font-size:36px;letter-spacing:2px">ASSEMBLIES, INC.</text>
  </svg>

  <svg class="card card--back" viewBox="0 0 1364 779" xmlns="http://www.w3.org/2000/svg" aria-label="Business card back">
    <rect width="1364" height="779" fill="var(--navy)"/>
    <circle class="backdrop-disc" cx="391" cy="349" r="335" fill="var(--navy-soft)"/>
    <polygon class="band-accent" points="0,570 537,570 669,709 1364,709 1364,779 0,779" fill="var(--red)"/>

    <text class="web-address" x="83" y="680">voltlineassemblies.example</text>

    <circle class="brand-dot" cx="1010" cy="292" r="72" fill="var(--white)"/>
    <text class="brand-name brand-name--white" x="1010" y="452">VOLTLINE</text>
    <text class="brand-name brand-name--white" x="1010" y="514" style="font-size:36px;letter-spacing:2px">ASSEMBLIES, INC.</text>
  </svg>

</main>
</body>
</html>
```